Brisk Haven Womens Shaving Foam (For sale in supermarkets).

We supply supermarkets with various products and now need a new design for a Ladies Shaving Foam Can. Soft Pink on the bottom of the can finishing of gradated into white. Needs to have a Shaving Foam swirl image also needs to have our Brisk Haven Logo. White base Can with mainly soft pink. I have mocked one up with Brisk Haven Logo in the middle similar to the Body Spray cans. Good Luck.
Target Market(s)
Females
Industry/Entity Type
Grocery
Colors
ffffff
e34197
e667a6
eea4c8
f9d9e8
Requirements
Must have
- White Can base with Pink colour tones
Nice to have
- Modern fresh feel
Should not have
- No dark colours soft pinks

```html
<!DOCTYPE html>
<html lang="en">
<head>
<meta charset="utf-8">
<title>Brisk Haven Sensitive Shaving Foam Label</title>
<link rel="stylesheet" href="https://fonts.googleapis.com/css2?family=Cinzel:wght@400;600;700&family=Marcellus&display=swap">
<style>
  :root {
    --white: #ffffff;
    --pink-deep: #e34197;
    --pink-mid: #e667a6;
    --pink-soft: #eea4c8;
    --pink-pale: #f9d9e8;
    --silver: #8e8f94;
    --frame: #d9d4d7;
  }
  html, body {
    margin: 0;
    padding: 0;
    width: 1200px;
    height: 1200px;
    overflow: hidden;
    background: var(--white);
  }
  .canvas {
    position: relative;
    width: 1200px;
    height: 1200px;
    background: var(--white);
  }
  .label {
    position: absolute;
    left: 336px;
    top: 50px;
    width: 528px;
    height: 1100px;
    box-sizing: border-box;
    border: 1px solid var(--frame);
    background: linear-gradient(180deg, #fdf6f9 0%, var(--white) 20%, #fdf3f7 55%, var(--pink-pale) 80%, #f4c9dc 100%);
    overflow: hidden;
  }
  .dancer-art {
    position: absolute;
    left: 84px;
    top: 31px;
    width: 308px;
    height: 719px;
    border-radius: 45% 45% 40% 40% / 30% 30% 20% 20%;
    background: radial-gradient(ellipse at 50% 40%, rgba(238,164,200,0.55) 0%, rgba(249,217,232,0.45) 45%, rgba(255,255,255,0) 75%);
  }
  .brand-name {
    position: absolute;
    left: 0;
    top: 400px;
    width: 100%;
    text-align: center;
    font-family: "Cinzel", serif;
    font-weight: 700;
    font-size: 64px;
    letter-spacing: 2px;
    color: var(--silver);
    margin: 0;
  }
  .product-line {
    position: absolute;
    left: 0;
    top: 510px;
    width: 100%;
    text-align: center;
    font-family: "Cinzel", serif;
    font-weight: 400;
    font-size: 36px;
    color: var(--pink-mid);
    margin: 0;
  }
  .foam-swirl {
    position: absolute;
    left: 173px;
    top: 764px;
    width: 182px;
    height: 150px;
    border-radius: 50% 50% 45% 45% / 40% 40% 55% 55%;
    background: radial-gradient(ellipse at 50% 55%, var(--white) 0%, var(--pink-pale) 45%, var(--pink-soft) 100%);
  }
  .variant {
    position: absolute;
    left: 0;
    top: 926px;
    width: 100%;
    text-align: center;
    font-family: "Cinzel", serif;
    font-size: 26px;
    color: var(--pink-mid);
    margin: 0;
  }
  .title-band {
    position: absolute;
    left: 40px;
    top: 971px;
    width: 448px;
    height: 58px;
    background: linear-gradient(90deg, rgba(238,164,200,0) 0%, var(--pink-soft) 30%, var(--pink-soft) 70%, rgba(238,164,200,0) 100%);
  }
  .product-type {
    position: absolute;
    left: 0;
    top: 978px;
    width: 100%;
    text-align: center;
    font-family: "Cinzel", serif;
    font-weight: 700;
    font-size: 36px;
    color: var(--white);
    margin: 0;
  }
  .net-content {
    position: absolute;
    left: 0;
    top: 1040px;
    width: 100%;
    text-align: center;
    font-family: "Marcellus", serif;
    font-size: 23px;
    color: var(--pink-mid);
    margin: 0;
  }
</style>
</head>
<body>
<div class="canvas">
  <section class="label">
    <div class="dancer-art" role="img" aria-label="Soft pink illustration of a graceful dancing woman with raised arms"></div>
    <h1 class="brand-name">Brisk Haven</h1>
    <p class="product-line">Soft Bloom</p>
    <div class="foam-swirl" role="img" aria-label="Pink and white swirl of shaving foam"></div>
    <p class="variant">SENSITIVE</p>
    <div class="title-band"></div>
    <p class="product-type">SHAVING FOAM</p>
    <p class="net-content">200 ml - 100g</p>
  </section>
</div>
</body>
</html>
```